Web Design Project

We need web design for a new baby products (nursery furniture) business in Australia.

The logo is already done, and I would like to reflect a similar theme throughout the website:
* Clean, white background.
* Use of lime green, purple and orange.
* Similar font to logo for headings
* FUNKY, FASHIONABLE, QUALITY feeling of website.

The main concept is to be attractive to discerning mums who are buying big items like a cot or chest of drawers. These are expensive items and will be considered the most important purchases for a newborn, so the website has to be enticing!!!
Updates

Hello,

Thank you for your submissions. I have received a few questions regarding the font and the coding of this website.

The job I am seeking is for design for an E-commerce store. The font was done by another pixel guild designer, so I do not know what type of font I am sorry.

I was hoping to have more designs by now, so please send them soon, this project is guaranteed!

I also ask you to read the brief properly please. The name of the business is Cradle Lane, as the logo says. The use of design that I have mentioned has only been demonstrated in a couple of designs submitted to me.

I look forward to seeing your work soon!

Kind Regards
Marla

Target Market(s)

Young mothers aged 25-45

Industry/Entity Type

Business

Requirements
Must have
• Must be funky, bright, energetic, attractive visually.
Nice to have
• I like the idea of some floral / design work in faded lime green, purple on some of the edges of different pages. Maybe islamic design? But has to be very fashionable.
Should not have
• Should not have any traditional ideas of baby websites.

ie- no stork, nappy images, teddybears etc.

```html
<!DOCTYPE html>
<html lang="en">
<head>
<meta charset="utf-8">
<title>Cradle Lane — Nursery Furniture</title>
<link rel="stylesheet" href="https://fonts.googleapis.com/css2?family=Arimo:wght@400;700&family=Archivo+Black&family=Roboto+Condensed:wght@400;700&family=Noto+Sans:wght@400;700&display=swap">
<style>
  :root {
    --lime-bg: #d3eb9a;
    --lime-frame: #e6f3c6;
    --purple: #a100c6;
    --purple-deep: #7a2a92;
    --purple-nav: #8d3aa3;
    --purple-soft: #f3e2f3;
    --purple-pale: #d9b4de;
    --green: #7fbf0a;
    --green-dark: #6aa300;
    --green-panel: #eef4dd;
    --green-row: #d8e8a9;
    --green-border: #d6e4b6;
    --yellow: #ffc000;
    --white: #ffffff;
    --ink: #111111;
    --ink-soft: #444444;
    --footer: #bdd68a;
  }
  * { margin: 0; padding: 0; box-sizing: border-box; }
  html, body { width: 1200px; height: 1160px; overflow: hidden; }
  body {
    position: relative;
    background: var(--lime-bg);
    font-family: "Arimo", Arial, sans-serif;
    color: var(--ink);
  }
  .abs { position: absolute; }

  /* top utility bar */
  .utility-bar { left: 0; top: 0; width: 1200px; height: 32px; background: var(--purple); color: var(--white); font-size: 12px; }
  .utility-links { position: absolute; left: 100px; top: 9px; letter-spacing: .2px; }
  .utility-cart { position: absolute; right: 100px; top: 9px; }
  .utility-cart b { font-weight: 700; }
  .trim-band { left: 0; top: 32px; width: 1200px; height: 24px; background: linear-gradient(#c98ad9, #e4d0ea); }

  /* page frame */
  .page-frame { left: 100px; top: 130px; width: 1000px; height: 956px; background: var(--lime-frame); border-radius: 14px 14px 0 0; }
  .page-sheet { left: 110px; top: 140px; width: 980px; height: 935px; background: var(--white); }
  .logo-tab { left: 483px; top: 70px; width: 300px; height: 160px; background: var(--white); border-radius: 150px 150px 0 0 / 90px 90px 0 0; box-shadow: 0 -10px 0 0 var(--lime-frame); }
  .brand { left: 483px; top: 100px; width: 300px; display: flex; align-items: center; justify-content: center; gap: 12px; }
  .brand-dot { width: 44px; height: 44px; border-radius: 50%; background: var(--green); }
  .brand-name { font-family: "Arimo", Arial, sans-serif; font-weight: 700; font-size: 36px; color: var(--purple); }

  /* navigation ribbon */
  .ribbon-end { top: 193px; width: 90px; height: 64px; }
  .ribbon-left { left: 136px; }
  .ribbon-right { left: 974px; }
  .main-nav { left: 176px; top: 180px; width: 847px; height: 63px; background: linear-gradient(#a24fb8, var(--purple-nav)); border-radius: 3px; display: flex; align-items: center; padding-left: 44px; font-family: "Noto Sans", sans-serif; font-size: 15px; color: var(--white); }
  .main-nav span { display: inline-block; }
  .main-nav .sep { width: 2px; height: 14px; border-left: 2px dotted rgba(255,255,255,.6); margin: 0 34px; }

  /* hero photos */
  .hero-photo { top: 274px; height: 286px; }
  .photo-cot { background: linear-gradient(160deg, #e9eef6, #d6c7b0 70%, #8b5a3a); }
  .photo-dresser { background: linear-gradient(170deg, #c7c49a, #e7e2d8 45%, #9c8f80); }
  .photo-room { background: linear-gradient(165deg, #e0c49a, #f2ead8 50%, #c8b7a0); }

  /* promo boxes */
  .promo-sale { left: 792px; top: 274px; width: 270px; height: 167px; background: radial-gradient(circle at 50% 40%, #e7fb8a, #b6e84a); border: 1px solid #a7d23d; text-align: center; }
  .sale-title { font-family: "Archivo Black", sans-serif; font-size: 62px; line-height: 1; color: #4c7a00; margin-top: 12px; letter-spacing: 2px; }
  .sale-sub { font-family: "Arimo", Arial, sans-serif; font-weight: 700; font-size: 31px; margin-top: 8px; }
  .btn-shop { display: inline-block; margin-top: 8px; width: 127px; height: 35px; background: var(--green); border-bottom: 3px solid #4f8a00; color: var(--white); font-family: "Roboto Condensed", sans-serif; font-size: 19px; line-height: 32px; }
  .promo-save { left: 792px; top: 455px; width: 270px; height: 104px; background: var(--yellow); border: 1px solid #f0a800; text-align: center; color: var(--white); }
  .save-title { font-family: "Archivo Black", sans-serif; font-size: 44px; line-height: 1; margin-top: 13px; letter-spacing: 1px; }
  .save-title em { font-style: normal; color: var(--purple); }
  .save-sub { font-family: "Roboto Condensed", sans-serif; font-size: 26px; margin-top: 5px; }

  /* products */
  .product-panel { left: 138px; top: 586px; width: 639px; height: 462px; background: var(--green-panel); border: 1px solid var(--green-border); }
  .product-card { width: 197px; height: 204px; background: var(--white); border: 1px solid var(--green-border); }
  .product-name { position: absolute; left: 18px; top: 13px; font-size: 14px; }
  .product-thumb { position: absolute; left: 18px; top: 36px; width: 160px; height: 76px; border: 1px solid #ccc; }
  .thumb-a { background: linear-gradient(90deg, #f4f4f4, #c9b6a2 70%, #8a4d36); }
  .thumb-b { background: linear-gradient(90deg, #d8a878, #f1e6d8 50%, #a87444); }
  .thumb-c { background: linear-gradient(90deg, #d9b07a, #f3e6cf 55%, #e5833b); }
  .thumb-d { background: linear-gradient(90deg, #b58652, #f0d66a 50%, #d39a54); }
  .thumb-e { background: linear-gradient(90deg, #8fa54c, #efece4 55%, #a8b37a); }
  .product-desc { position: absolute; left: 18px; top: 121px; font-size: 12px; line-height: 17px; color: var(--ink); }
  .product-buy { position: absolute; left: 18px; top: 164px; display: flex; height: 25px; font-family: "Roboto Condensed", sans-serif; font-size: 15px; line-height: 25px; }
  .price { width: 70px; background: var(--yellow); text-align: center; }
  .add-cart { width: 91px; background: var(--green); color: var(--white); text-align: center; }

  /* side boxes */
  .side-head { height: 38px; color: var(--white); font-family: "Roboto Condensed", sans-serif; font-size: 18px; line-height: 40px; padding-left: 18px; }
  .cart-box { left: 792px; top: 587px; width: 270px; height: 156px; background: var(--green-panel); border: 1px solid var(--green-border); }
  .cart-box .side-head { background: linear-gradient(#95cc17, var(--green-dark)); }
  .cart-empty { position: absolute; left: 18px; top: 47px; font-size: 14px; }
  .cart-row { position: absolute; left: 18px; width: 232px; height: 26px; background: var(--green-row); font-size: 12px; line-height: 26px; padding: 0 16px 0 11px; display: flex; justify-content: space-between; }
  .cart-checkout { position: absolute; left: 18px; top: 129px; font-size: 14px; color: var(--green-dark); }
  .category-box { left: 792px; top: 757px; width: 270px; height: 291px; background: var(--purple-soft); border: 1px solid #e2c9e4; }
  .category-box .side-head { background: var(--purple-deep); }
  .category-group { position: absolute; left: 18px; top: 50px; width: 232px; height: 26px; background: var(--purple-pale); color: var(--white); font-weight: 700; font-size: 13px; line-height: 26px; padding-left: 12px; letter-spacing: .3px; }
  .category-list { position: absolute; left: 18px; top: 80px; width: 230px; list-style: none; font-size: 12px; color: #333; }
  .category-list li { height: 32px; line-height: 26px; border-bottom: 1px solid #ddc5df; padding-left: 19px; position: relative; letter-spacing: .2px; }
  .category-list li:last-child { border-bottom: none; }
  .category-list li::before { content: "›"; position: absolute; left: 2px; top: 0; color: #555; }
  .btn-more { position: absolute; left: 20px; top: 242px; width: 107px; height: 25px; background: var(--purple-deep); color: var(--white); font-size: 14px; line-height: 25px; text-align: center; }

  /* footer */
  .site-footer { left: 0; top: 1108px; width: 1200px; height: 52px; background: var(--footer); font-size: 12px; color: #555; }
  .footer-copy { position: absolute; left: 101px; top: 16px; }
  .footer-links { position: absolute; right: 102px; top: 16px; letter-spacing: .2px; }
</style>
</head>
<body>

<header>
  <div class="abs utility-bar">
    <div class="utility-links">My Account &nbsp;|&nbsp; My Wishlist &nbsp;|&nbsp; My Cart &nbsp;|&nbsp; Checkout &nbsp;|&nbsp; Log In</div>
    <div class="utility-cart"><b>Shopping Cart :</b> 0 Products | Show Cart</div>
  </div>
  <div class="abs trim-band" role="img" aria-label="Decorative floral trim border"></div>
</header>

<div class="abs page-frame"></div>
<div class="abs logo-tab"></div>
<div class="abs page-sheet"></div>

<div class="abs brand">
  <span class="brand-dot"></span>
  <span class="brand-name">Cradle Lane</span>
</div>

<svg class="abs ribbon-end ribbon-left" viewBox="0 0 90 64" aria-hidden="true">
  <polygon points="0,0 90,0 90,64 12,64 28,32" fill="#7a2b8f"/>
</svg>
<svg class="abs ribbon-end ribbon-right" viewBox="0 0 90 64" aria-hidden="true">
  <polygon points="0,0 90,0 62,32 78,64 0,64" fill="#7a2b8f"/>
</svg>
<nav class="abs main-nav">
  <span>Home</span><span class="sep"></span>
  <span>Products</span><span class="sep"></span>
  <span>Merchents</span><span class="sep"></span>
  <span>Wishlist</span><span class="sep"></span>
  <span>Specials</span><span class="sep"></span>
  <span>Contact us</span>
</nav>

<div class="abs hero-photo photo-cot" style="left:138px;width:208px" role="img" aria-label="White cot with canopy in a nursery"></div>
<div class="abs hero-photo photo-dresser" style="left:354px;width:207px" role="img" aria-label="White chest of drawers with changing top"></div>
<div class="abs hero-photo photo-room" style="left:569px;width:208px" role="img" aria-label="Wooden cot with toys in a bright nursery"></div>

<aside class="abs promo-sale">
  <div class="sale-title">SALE</div>
  <div class="sale-sub">upto 50% off</div>
  <span class="btn-shop">SHOP NOW</span>
</aside>
<aside class="abs promo-save">
  <div class="save-title">SAVE <em>20%</em></div>
  <div class="save-sub">ON SELECTED ITEMS</div>
</aside>

<section class="abs product-panel"></section>

<article class="abs product-card" style="left:153px;top:608px">
  <div class="product-name">Product_000074</div>
  <div class="product-thumb thumb-a" role="img" aria-label="White cot"></div>
  <p class="product-desc">Lorem ipsum dolor sit amet,<br>consectetuer adipiscing elit.</p>
  <div class="product-buy"><span class="price">$ 699.00</span><span class="add-cart">Add to Cart</span></div>
</article>
<article class="abs product-card" style="left:360px;top:608px">
  <div class="product-name">Product_000074</div>
  <div class="product-thumb thumb-b" role="img" aria-label="Wooden nursery wardrobe"></div>
  <p class="product-desc">Lorem ipsum dolor sit amet,<br>consectetuer adipiscing elit.</p>
  <div class="product-buy"><span class="price">$ 699.00</span><span class="add-cart">Add to Cart</span></div>
</article>
<article class="abs product-card" style="left:567px;top:608px">
  <div class="product-name">Product_000074</div>
  <div class="product-thumb thumb-c" role="img" aria-label="Pine cot with orange bedding"></div>
  <p class="product-desc">Lorem ipsum dolor sit amet,<br>consectetuer adipiscing elit.</p>
  <div class="product-buy"><span class="price">$ 699.00</span><span class="add-cart">Add to Cart</span></div>
</article>
<article class="abs product-card" style="left:153px;top:822px">
  <div class="product-name">Product_000074</div>
  <div class="product-thumb thumb-d" role="img" aria-label="Cot with yellow canopy"></div>
  <p class="product-desc">Lorem ipsum dolor sit amet,<br>consectetuer adipiscing elit.</p>
  <div class="product-buy"><span class="price">$ 699.00</span><span class="add-cart">Add to Cart</span></div>
</article>
<article class="abs product-card" style="left:360px;top:822px">
  <div class="product-name">Product_000074</div>
  <div class="product-thumb thumb-e" role="img" aria-label="White chest of drawers"></div>
  <p class="product-desc">Lorem ipsum dolor sit amet,<br>consectetuer adipiscing elit.</p>
  <div class="product-buy"><span class="price">$ 699.00</span><span class="add-cart">Add to Cart</span></div>
</article>
<article class="abs product-card" style="left:567px;top:822px">
  <div class="product-name">Product_000074</div>
  <div class="product-thumb thumb-a" role="img" aria-label="White cot"></div>
  <p class="product-desc">Lorem ipsum dolor sit amet,<br>consectetuer adipiscing elit.</p>
  <div class="product-buy"><span class="price">$ 699.00</span><span class="add-cart">Add to Cart</span></div>
</article>

<aside class="abs cart-box">
  <div class="side-head">CART</div>
  <div class="cart-empty">No Products</div>
  <div class="cart-row" style="top:67px"><span>Shipping</span><span>$ 0.00</span></div>
  <div class="cart-row" style="top:96px"><span>Total</span><span>$ 0.00</span></div>
  <div class="cart-checkout">Check Out</div>
</aside>

<aside class="abs category-box">
  <div class="side-head">PRODUCT CATEGORIES</div>
  <div class="category-group">Lorem Ipsum</div>
  <ul class="category-list">
    <li>Times change and bring these</li>
    <li>Changes in all spheres of life.</li>
    <li>Fashion seems to be perhaps one.</li>
    <li>Of the most changeable pheno.</li>
    <li>Enons of all times It reflects.</li>
  </ul>
  <span class="btn-more">More Products</span>
</aside>

<footer class="abs site-footer">
  <div class="footer-copy">Copyright © 2012 Cradle Lane. All rights reserved</div>
  <div class="footer-links">Home &nbsp;|&nbsp; Products &nbsp;|&nbsp; New Products &nbsp;|&nbsp; Stock &nbsp;|&nbsp; Specials &nbsp;|&nbsp; Contact Us</div>
</footer>

</body>
</html>
```